Patient Engagement Solution

We need an attractive and easy-to-use GUI for patients and clinicians, which includes screens and icons. The application has been named TVNwell. I have our corporate logo attached as well.
I have attached the screens that the developer has used to create the solution, but we all know they miss the target when it comes to the creative stuff.
If it helps, I can supply some competitor's screens as a guide - please let me know.

Target Market(s)

Patients and Clinicians

Industry/Entity Type

Healthcare/Hospitals

Font styles to use
Other font styles liked:
• Easy to Read

Requirements
Must have
• Attractive, easy to use graphical user interface. Screen size is usually 22" 16:9
Nice to have
• Inviting and interesting look
Should not have
• Complicated hard to navigate screens

```html
<!DOCTYPE html>
<html lang="en">
<head>
<meta charset="utf-8">
<title>TVNwell – Patient Engagement Screens</title>
<link href="https://fonts.googleapis.com/css2?family=Outfit:wght@400;500;600&family=Encode+Sans:wght@400;500&family=Space+Mono&display=swap" rel="stylesheet">
<style>
:root{
  --bar:#1e1e1e;
  --white:#ffffff;
  --red:#e3202a;
  --red-deep:#b80d1a;
  --hero-a:#07086a;
  --hero-b:#00457a;
  --nav-a:#1d2550;
  --nav-b:#16384f;
  --panel-a:#1f2242;
  --panel-b:#1b2d3d;
  --gap:#ffffff;
}
*{margin:0;padding:0;box-sizing:border-box}
html,body{width:1200px;height:2275px;overflow:hidden;background:var(--gap)}
body{position:relative;font-family:"Outfit",sans-serif;color:var(--white)}
.screen{position:absolute;left:0;width:1200px}
.topbar{position:absolute;left:0;top:0;width:1200px;height:62px;background:var(--bar)}
.brand{position:absolute;left:0;right:0;top:14px;text-align:center;font-family:"Outfit",sans-serif;font-weight:600;font-size:25px;color:var(--white);letter-spacing:-.3px}
.bar-time,.bar-date{position:absolute;top:22px;font-family:"Space Mono",monospace;font-size:14px}
.bar-time{left:51px}
.bar-date{right:51px}

/* home */
.home{top:0;height:675px}
.hero{position:absolute;top:62px;left:0;width:1200px;height:461px;background:linear-gradient(100deg,var(--hero-a) 0%,#06216a 45%,var(--hero-b) 100%)}
.clock{position:absolute;top:68px;left:0;right:0;text-align:center;font-family:"Encode Sans",sans-serif;font-weight:500;font-size:82px;letter-spacing:3px}
.date{position:absolute;top:162px;left:0;right:0;text-align:center;font-family:"Encode Sans",sans-serif;font-size:31px;letter-spacing:.5px}
.nav{position:absolute;top:523px;left:0;width:1200px;height:152px;background:linear-gradient(90deg,var(--nav-a),var(--nav-b))}
.nav-item{position:absolute;top:40px;width:160px;margin-left:-80px;text-align:center;font-size:18px;font-weight:500}
.nav-item svg{display:block;margin:0 auto 4px;width:46px;height:46px}
.nav-item.active{color:var(--red)}

/* inner pages */
.page-body{position:absolute;top:62px;left:0;width:1200px;background:linear-gradient(100deg,var(--panel-a),var(--panel-b))}
.back{position:absolute;left:51px;top:32px;display:flex;align-items:center;gap:20px;font-size:17px}
.page-title{position:absolute;top:26px;left:0;right:0;text-align:center;font-size:39px;font-weight:500}

.apps{top:800px;height:674px}
.apps .page-body{height:612px}
.app{position:absolute;width:180px;margin-left:-90px;text-align:center;font-size:19px;font-weight:500}
.app .tile{height:110px;display:flex;align-items:center;justify-content:center}
.app.selected .tile{background:var(--red-deep);border:3px solid var(--white);border-radius:8px;outline:2px solid rgba(255,255,255,.25)}
.app .label{margin-top:14px}
.app svg{width:74px;height:74px}
.pager{position:absolute;left:1000px;top:530px;display:flex;gap:4px;align-items:center}
.pager .on{width:30px;height:6px;border-radius:3px;background:var(--red)}
.pager .dot{width:6px;height:6px;border-radius:50%;background:var(--white)}

.langs{top:1600px;height:675px}
.langs .page-body{height:613px}
.lang{position:absolute;width:238px;height:60px;border:1.5px solid var(--white);border-radius:3px;display:flex;align-items:center;font-size:25px;box-shadow:0 2px 0 rgba(227,32,42,.35)}
.lang svg{margin-left:13px;width:50px;height:35px;flex:none}
.lang span{margin-left:33px}
</style>
</head>
<body>

<!-- Home screen -->
<section class="screen home">
  <header class="topbar"><div class="brand">TVNwell</div></header>
  <div class="hero">
    <div class="clock">04:04</div>
    <div class="date">Friday 07 September 2023</div>
  </div>
  <nav class="nav">
    <div class="nav-item active" style="left:79px">
      <svg viewBox="0 0 46 46"><path d="M4 18 Q4 14 8 12 L20 3 Q23 1 26 3 L38 12 Q42 14 42 18 L42 38 Q42 44 36 44 L10 44 Q4 44 4 38Z" fill="#e3202a"/><path d="M16 29 Q23 36 30 29" stroke="#1d2550" stroke-width="3" fill="none" stroke-linecap="round"/></svg>Home</div>
    <div class="nav-item" style="left:255px">
      <svg viewBox="0 0 46 46" fill="none" stroke="#fff" stroke-width="3"><path d="M4 14 V8 H42 V36 H26"/><path d="M4 20 a18 18 0 0 1 18 18 M4 27 a11 11 0 0 1 11 11"/><circle cx="5" cy="37" r="1.5" fill="#fff"/><path d="M16 42 H30"/></svg>Entertainment</div>
    <div class="nav-item" style="left:435px">
      <svg viewBox="0 0 46 46" fill="none" stroke="#fff" stroke-width="3"><path d="M12 10 H34 Q42 10 43 22 L44 32 Q44 38 38 36 L32 30 H14 L8 36 Q2 38 2 32 L3 22 Q4 10 12 10Z"/><path d="M10 20 H18 M14 16 V24"/><circle cx="30" cy="18" r="1.5" fill="#fff"/><circle cx="34" cy="22" r="1.5" fill="#fff"/><circle cx="28" cy="23" r="1.5" fill="#fff"/></svg>Games</div>
    <div class="nav-item" style="left:589px">
      <svg viewBox="0 0 46 46" fill="none" stroke="#fff" stroke-width="3"><path d="M16 3 H30 V16 H43 V30 H30 V43 H16 V30 H3 V16 H16Z"/><path d="M3 24 H15 L19 17 L25 31 L29 24 H43"/></svg>My Care</div>
    <div class="nav-item" style="left:763px">
      <svg viewBox="0 0 46 46" fill="none" stroke="#fff" stroke-width="3"><rect x="4" y="4" width="15" height="15"/><circle cx="33" cy="11.5" r="8"/><rect x="4" y="26" width="15" height="15"/><rect x="26" y="26" width="15" height="15"/></svg>Application</div>
    <div class="nav-item" style="left:943px">
      <svg viewBox="0 0 46 46" fill="none" stroke="#fff" stroke-width="2.5"><circle cx="15" cy="15" r="12"/><path d="M3 15 H27 M15 3 Q8 15 15 27 M15 3 Q22 15 15 27"/><path d="M14 44 L21 26 L28 44 M16 38 H26" /><path d="M30 24 H44 M37 20 V24 M32 30 H42 L37 35 V44 L34 42"/></svg>Language</div>
    <div class="nav-item" style="left:1110px">
      <svg viewBox="0 0 46 46" fill="none" stroke="#fff" stroke-width="3.5"><path d="M23 3 L28 8 L35 6 L37 13 L43 17 L40 23 L43 29 L37 33 L35 40 L28 38 L23 43 L18 38 L11 40 L9 33 L3 29 L6 23 L3 17 L9 13 L11 6 L18 8Z" stroke-linejoin="round"/><circle cx="23" cy="23" r="7"/></svg>Settings</div>
  </nav>
</section>

<!-- Applications screen -->
<section class="screen apps">
  <header class="topbar"><div class="bar-time">04:04 am</div><div class="brand">TVNwell</div><div class="bar-date">07 - 11 - 2023</div></header>
  <div class="page-body">
    <div class="back"><svg width="28" height="22" viewBox="0 0 28 22" fill="none" stroke="#fff" stroke-width="1.6"><path d="M7 2 L2 7 L7 12"/><path d="M2 7 H18 Q26 7 26 14 Q26 20 18 20 H12"/></svg>Back to Home</div>
    <h1 class="page-title">Applications</h1>

    <div class="app" style="left:181px;top:115px"><div class="tile"><svg viewBox="0 0 74 74" fill="none" stroke="#fff" stroke-width="5"><path d="M34 14 A26 26 0 1 0 64 44 A20 20 0 0 1 34 14Z" stroke-linejoin="round"/><path d="M52 8 H62 L52 20 H62 M38 30 H46 L38 40 H46" stroke-width="3"/></svg></div><div class="label">RELAX</div></div>
    <div class="app" style="left:390px;top:115px"><div class="tile"><svg viewBox="0 0 74 74" fill="none" stroke="#fff" stroke-width="4"><circle cx="37" cy="37" r="30"/><path d="M7 37 H67 M11 22 H63 M11 52 H63 M37 7 Q18 37 37 67 M37 7 Q56 37 37 67 M37 7 V67"/></svg></div><div class="label">INTERNET</div></div>
    <div class="app selected" style="left:600px;top:115px"><div class="tile"><svg viewBox="0 0 74 74"><rect x="8" y="12" width="44" height="56" rx="5" fill="#fff"/><rect x="20" y="6" width="20" height="12" rx="3" fill="#fff" stroke="#b80d1a" stroke-width="3"/><path d="M20 36 H32 M26 30 V42 M18 50 H42 M18 58 H42" stroke="#b80d1a" stroke-width="3.5"/><circle cx="63" cy="28" r="4" fill="#fff"/><path d="M59 36 H67 V62 L63 68 L59 62Z" fill="#fff"/></svg></div><div class="label">CLINICAL</div></div>
    <div class="app" style="left:809px;top:115px"><div class="tile"><svg viewBox="0 0 74 74" fill="none" stroke="#fff" stroke-width="4"><path d="M6 46 H68"/><path d="M12 46 Q14 60 37 60 Q60 60 62 46"/><path d="M25 20 Q21 25 25 30 Q29 35 25 38 M37 18 Q33 23 37 28 Q41 33 37 36 M49 20 Q45 25 49 30 Q53 35 49 38" stroke-width="3"/></svg></div><div class="label">MEAL</div></div>
    <div class="app" style="left:1018px;top:115px"><div class="tile"><svg viewBox="0 0 74 74" fill="none" stroke="#fff" stroke-width="5" stroke-linejoin="round"><path d="M37 18 Q24 8 5 10 V60 Q24 58 37 68 Q50 58 69 60 V10 Q50 8 37 18Z"/><path d="M37 18 V68"/></svg></div><div class="label">BOOKS</div></div>

    <div class="app" style="left:181px;top:322px"><div class="tile"><svg viewBox="0 0 74 74" fill="none" stroke="#fff" stroke-width="4.5" stroke-linejoin="round"><path d="M14 8 L26 8 L30 22 L22 28 Q28 42 44 50 L50 42 L64 46 L64 58 Q60 66 48 64 Q20 56 10 26 Q8 14 14 8Z"/><path d="M42 10 A22 22 0 0 1 62 30 M42 20 A12 12 0 0 1 52 30" stroke-width="3.5" stroke-linecap="round"/></svg></div><div class="label">CALL</div></div>
    <div class="app" style="left:390px;top:322px"><div class="tile"><svg viewBox="0 0 74 74" fill="none" stroke="#fff" stroke-width="4.5" stroke-linejoin="round"><rect x="10" y="32" width="54" height="32" rx="2"/><path d="M8 22 L60 10 L63 22 L11 34Z"/><path d="M22 20 L28 30 M36 16 L42 27 M50 13 L56 24" stroke-width="3"/></svg></div><div class="label">MOVIES</div></div>
    <div class="app" style="left:600px;top:322px"><div class="tile"><svg viewBox="0 0 74 74" fill="none" stroke="#fff" stroke-width="4.5"><path d="M24 58 V16 L64 8 V50"/><path d="M24 28 L64 20"/><circle cx="16" cy="58" r="8"/><circle cx="56" cy="50" r="8"/></svg></div><div class="label">MUSIC</div></div>
    <div class="app" style="left:809px;top:322px"><div class="tile"><svg viewBox="0 0 74 74" fill="none" stroke="#fff" stroke-width="4.5"><rect x="6" y="20" width="62" height="46" rx="9"/><path d="M18 20 L60 6"/><path d="M20 34 H54" stroke-width="3.5"/><circle cx="22" cy="50" r="4.5"/><path d="M34 50 H56" stroke-width="3.5"/></svg></div><div class="label">RADIO</div></div>
    <div class="app" style="left:1018px;top:322px"><div class="tile"><svg viewBox="0 0 74 74" fill="none" stroke="#fff" stroke-width="4.5" stroke-linejoin="round"><path d="M20 16 H54 Q66 16 68 36 L69 52 Q68 62 58 58 L50 48 H24 L16 58 Q6 62 5 52 L6 36 Q8 16 20 16Z"/><path d="M16 32 H30 M23 25 V39" stroke-width="4"/><circle cx="48" cy="28" r="2.5" fill="#fff"/><circle cx="55" cy="34" r="2.5" fill="#fff"/><circle cx="46" cy="38" r="2.5" fill="#fff"/></svg></div><div class="label">GAMES</div></div>

    <div class="pager"><div class="on"></div><div class="dot"></div><div class="dot"></div><div class="dot"></div></div>
  </div>
</section>

<!-- Languages screen -->
<section class="screen langs">
  <header class="topbar"><div class="bar-time">04:04 am</div><div class="brand">TVNwell</div><div class="bar-date">07 - 11 - 2023</div></header>
  <div class="page-body">
    <div class="back"><svg width="28" height="22" viewBox="0 0 28 22" fill="none" stroke="#fff" stroke-width="1.6"><path d="M7 2 L2 7 L7 12"/><path d="M2 7 H18 Q26 7 26 14 Q26 20 18 20 H12"/></svg>Back to Home</div>
    <h1 class="page-title">Languages</h1>

    <div class="lang" style="left:67px;top:168px"><svg viewBox="0 0 50 35"><rect width="50" height="35" fill="#fff"/><g fill="#d22f3c"><rect y="0" width="50" height="2.7"/><rect y="5.4" width="50" height="2.7"/><rect y="10.8" width="50" height="2.7"/><rect y="16.2" width="50" height="2.7"/><rect y="21.6" width="50" height="2.7"/><rect y="27" width="50" height="2.7"/><rect y="32.3" width="50" height="2.7"/></g><rect width="22" height="18.9" fill="#3c3b6e"/></svg><span>English</span></div>
    <div class="lang" style="left:343px;top:168px"><svg viewBox="0 0 50 35"><rect width="17" height="35" fill="#1a2a6c"/><rect x="17" width="16" height="35" fill="#fff"/><rect x="33" width="17" height="35" fill="#d52b2e"/></svg><span>France</span></div>
    <div class="lang" style="left:618px;top:168px"><svg viewBox="0 0 50 35"><rect width="50" height="35" fill="#fff"/><circle cx="25" cy="17.5" r="10" fill="#c8102e"/></svg><span>Japanese</span></div>
    <div class="lang" style="left:894px;top:168px"><svg viewBox="0 0 50 35"><rect width="17" height="35" fill="#1e9a4a"/><rect x="17" width="16" height="35" fill="#fff"/><rect x="33" width="17" height="35" fill="#d52b3a"/></svg><span>Italian</span></div>

    <div class="lang" style="left:67px;top:276px"><svg viewBox="0 0 50 35"><rect width="50" height="35" fill="#c60b1e"/><rect y="9" width="50" height="17" fill="#ffc400"/></svg><span>Spanish</span></div>
    <div class="lang" style="left:343px;top:276px"><svg viewBox="0 0 50 35"><rect width="50" height="35" fill="#ee1c25"/><path d="M9 4 L10.5 8.5 L15 8.5 L11.5 11 L13 15.5 L9 12.8 L5 15.5 L6.5 11 L3 8.5 L7.5 8.5Z" fill="#ffde00"/><circle cx="18" cy="4" r="1" fill="#ffde00"/><circle cx="21" cy="8" r="1" fill="#ffde00"/><circle cx="21" cy="12" r="1" fill="#ffde00"/><circle cx="18" cy="15" r="1" fill="#ffde00"/></svg><span>Chinese</span></div>
    <div class="lang" style="left:618px;top:276px"><svg viewBox="0 0 50 35"><rect width="50" height="35" fill="#da251d"/><path d="M25 7 L27.4 14.3 L35 14.3 L28.8 18.8 L31.2 26 L25 21.5 L18.8 26 L21.2 18.8 L15 14.3 L22.6 14.3Z" fill="#ffff00"/></svg><span>Vietnamese</span></div>
    <div class="lang" style="left:894px;top:276px"><svg viewBox="0 0 50 35"><rect width="50" height="12" fill="#000"/><rect y="12" width="50" height="11" fill="#dd0000"/><rect y="23" width="50" height="12" fill="#ffce00"/></svg><span>German</span></div>

    <div class="lang" style="left:343px;top:384px"><svg viewBox="0 0 50 35"><rect width="50" height="12" fill="#ff9933"/><rect y="12" width="50" height="11" fill="#fff"/><rect y="23" width="50" height="12" fill="#138808"/><circle cx="25" cy="17.5" r="4" fill="none" stroke="#000080" stroke-width="1"/></svg><span>Hindi</span></div>
    <div class="lang" style="left:618px;top:384px"><svg viewBox="0 0 50 35"><rect width="50" height="35" fill="#006c35"/><path d="M14 24 H36" stroke="#fff" stroke-width="1.2"/></svg><span>Arabic</span></div>
  </div>
</section>

</body>
</html>
```